Brochure Design- Targeted at Property Developers

We are the largest Conveyancing (property law) firm in the state of Victoria, Australia.

We need a very sophisticated brochure to enable us to take the next step and compete with law firms for property developer clients.

Much about us can be found on our website (inlcuding logos, photos, etc) www.brindlecove.com.au but our business name is Brindlecove- Marlow Reach not just Brindlecove. ALSO I HAVE ATTACHED MANY PHOTOS OF OUR STAFF AND SOME LOGOS TO HELP!!

Size: fold (A3 double sided so that there is 4 A4 pages)

Copy:

This can be played with by the designer to spread across the 4 pages. Ideally the front page will be very minimalistic and not mention our brand (or at least the brand should not dominate):

Page 1: Do property developers have a genuine alternative to high legal fees?

Page 2 and 3:

- 100% of our developer clients recommend us
- We already look after the Conveyancing needs of more developers in Victoria than any other Conveyancing firm
- Industry benchmark off- the- plan contracts (tailored to the requirements of each development). Our special conditions (including variations, rebates and resale restrictions) are carefully chosen to protect the interests of our vendors while being commercially sensitive to ensure sales are not lost unnecessarily
- Expert in guiding developers from first time dual occupancies to seasoned developers of large scale land and highrise projects
- Our large team and highly refined systems ensure fastest possible settlement times after subdivision registration
- We are available to train your project marketers on completing and executing contracts so that sales are not delayed or lost
- Establishment of interest bearing trust accounts
- Before you buy a development site have us thoroughly investigate the contract and vendors statement. We can then conduct the purchase settlement on your behalf.
- We have the friendliest and most efficient staff. Every dealing you have with our dedicated Development Division will be prompt, professional and impressive. You will never need to follow us up!
- Highly experienced Conveyancers with the security of full Solicitor support

Please consider us next time you need Conveyancing.

Services options:
- Use us from contract preparation to settlement or;
- Have your Solicitor prepare the contract and use us as an alternative for the settlement stage only. Many Solicitors recommend us for this service already
- Fast subdivision lodgements (including obtaining mortgagee’s consent, Solicitor preparation of Land Titles Office application, owners corporation establishment)

Page 4: Just our contact details (see our website)

The design should make us look highly professional, conservative, yet cutting edge.
Updates

Target Market(s)

Property developers of small to medium sized land and unit developments

Industry/Entity Type

Security

Requirements
Must have
• - Our logo and contact details as well as the copy above.
Nice to have
• - Pictures of land sites, highrise buildings under construction
Should not have
• I really dislike overly corny photos where everyone is fake and smiling. Other photos would be great but not too cheesy.

```html
<!DOCTYPE html>
<html lang="en">
<head>
<meta charset="utf-8">
<title>Brindlecove Marlow Reach – Developer Brochure</title>
<link rel="stylesheet" href="https://fonts.googleapis.com/css2?family=Arimo:wght@400;700&display=swap">
<style>
  :root {
    --navy: #2b3a97;
    --red: #d4242b;
    --deep-red: #a51a20;
    --ink: #2a1416;
    --white: #ffffff;
    --paper: #ffffff;
    --label: #333333;
  }
  * { box-sizing: border-box; margin: 0; padding: 0; }
  html, body { width: 900px; height: 1200px; overflow: hidden; background: var(--paper); }
  body { position: relative; font-family: "Arimo", Arial, sans-serif; color: var(--white); }
  .panel { position: absolute; }
  .brand { font-weight: 700; color: var(--white); line-height: 1.05; }
  .brand-square { display: inline-block; width: 9px; height: 9px; background: var(--white); margin-right: 6px; vertical-align: 1px; }
  .page-label { position: absolute; font-size: 11px; color: var(--label); }

  /* Back cover */
  .back-cover { left: 70px; top: 36px; width: 380px; height: 530px; background: var(--navy); }
  .back-cover .brand { position: absolute; left: 48px; top: 36px; font-size: 15px; }
  .contact { position: absolute; left: 48px; top: 318px; font-size: 11.5px; line-height: 1.38; }
  .contact p + p { margin-top: 12px; }

  /* Front cover */
  .front-cover { left: 450px; top: 36px; width: 380px; height: 530px; background: var(--navy); }
  .front-cover .red-band { position: absolute; left: 34px; top: 0; width: 30px; height: 100%; background: var(--red); }
  .front-cover .photo { position: absolute; left: 64px; top: 0; width: 316px; height: 100%;
    background: linear-gradient(165deg, #c9d6ea 0%, #7f97c2 35%, #4a6496 65%, #9aa6b6 100%); }
  .cover-card { position: absolute; left: 218px; top: 222px; width: 162px; height: 130px; background: var(--navy); padding: 14px 12px; }
  .cover-card .brand { font-size: 11px; margin-bottom: 24px; text-align: right; }
  .cover-card .question { font-size: 13.5px; line-height: 1.22; }

  /* Page 2 */
  .page-two { left: 70px; top: 620px; width: 380px; height: 530px; }
  .page-two .photo { position: absolute; inset: 0;
    background: linear-gradient(200deg, #dfe7f2 0%, #8aa3cc 30%, #3f5f98 60%, #6f7f99 100%); }
  .services-card { position: absolute; left: 186px; top: 110px; width: 194px; height: 370px; background: var(--red); padding: 14px 16px; }
  .services-card .brand { font-size: 12px; text-align: right; margin-bottom: 18px; }
  .services-card h3 { font-weight: 400; font-size: 13px; margin-bottom: 6px; }
  .services-card p { font-size: 10px; line-height: 1.3; margin-bottom: 10px; }
  .services-card .closing { font-size: 14px; line-height: 1.25; margin-top: 16px; }

  /* Page 3 */
  .page-three { left: 450px; top: 620px; width: 380px; height: 530px; background: var(--red); }
  .page-three .navy-band { position: absolute; right: 0; top: 0; width: 30px; height: 100%; background: var(--navy); }
  .headline { position: absolute; left: 36px; top: 18px; width: 300px; font-weight: 400; font-size: 33px; line-height: 1.12; }
  .lead { position: absolute; left: 36px; top: 132px; width: 300px; font-size: 13px; line-height: 1.3; }
  .column { position: absolute; width: 142px; font-size: 9.5px; line-height: 1.3; color: var(--ink); }
  .column p { margin-bottom: 9px; }
  .column.left { left: 36px; top: 204px; }
  .column.right { left: 198px; top: 204px; }
  .column.muted { color: var(--deep-red); }
  .column.left.muted { top: 348px; }
  .column.right.muted { top: 348px; }
</style>
</head>
<body>

  <section class="panel back-cover" aria-label="Back cover">
    <div class="brand"><span class="brand-square"></span>Brindlecove<br>Marlow Reach</div>
    <div class="contact">
      <p>Level 4, 18 Alder Crescent<br>Melbourne 3004 Victoria<br>Australia (Off Harwood Road)</p>
      <p>Postal: PO Box 4120<br>Harwood Road Central Melbourne 8008<br>DX Postal: DX 41876 South Melbourne</p>
      <p>Phone: (03) 9555 0142<br>International: +61 3 9555 0142<br>Fax: (03) 9555 0187<br>International Fax: +61 3 9555 0187<br>Email: marlowreach@brindlecove.com.au</p>
    </div>
  </section>
  <span class="page-label" style="left:70px;top:576px;">Back Cover</span>

  <section class="panel front-cover" aria-label="Front cover">
    <div class="red-band"></div>
    <div class="photo" role="img" aria-label="Photograph of a glass highrise tower seen from street level against a blue sky"></div>
    <div class="cover-card">
      <div class="brand">Brindlecove<br>Marlow Reach</div>
      <p class="question">Do property developers have a genuine alternative to high legal fees ?</p>
    </div>
  </section>
  <span class="page-label" style="left:752px;top:576px;">Front Cover</span>

  <section class="panel page-two" aria-label="Second page">
    <div class="photo" role="img" aria-label="Photograph of highrise buildings under construction with a tower crane"></div>
    <div class="services-card">
      <div class="brand">Brindlecove<br>Marlow Reach</div>
      <h3>Services options:</h3>
      <p>Use us from contract preparation to settlement or;</p>
      <p>Have your Solicitor prepare the contract and use us as an alternative for the settlement stage only. Many Solicitors recommend us for this service already.</p>
      <p>Fast subdivision lodgements (including obtaining mortgagee’s consent, Solicitor preparation of Land Titles Office application, owners corporation establishment).</p>
      <p class="closing">Please consider us next time you need Conveyancing.</p>
    </div>
  </section>
  <span class="page-label" style="left:70px;top:1162px;">2nd Page</span>

  <section class="panel page-three" aria-label="Third page">
    <div class="navy-band"></div>
    <h1 class="headline">100% of our developer clients recommend us.</h1>
    <p class="lead">We already look after the conveyancing needs of more developers in victoria than any other conveyancing firm.</p>
    <div class="column left">
      <p>Industry benchmark off-the-plan contracts (tailored to the requirements of each development). Our special conditions (including variations, rebates and resale restrictions) are carefully chosen to protect the interests of our vendors while being commercially sensitive to ensure sales are not lost unnecessarily.</p>
    </div>
    <div class="column right">
      <p>Expert in guiding developers from first time dual occupancies to seasoned developers of large scale land and high-rise projects.</p>
      <p>Our large team and highly refined systems ensure fastest possible settlement times after subdivision registration.</p>
    </div>
    <div class="column left muted">
      <p>Before you buy a development site have us thoroughly investigate the contract and vendors statement. We can then conduct the purchase settlement on your behalf.</p>
      <p>We have the friendliest and most efficient staff. Every dealing with our Development Division will be prompt, professional and impressive. You will never need to follow us up!</p>
    </div>
    <div class="column right muted">
      <p>We are available to train your project marketers on completing and executing contracts so that sales are not delayed or lost.</p>
      <p>Establishment of interest bearing trust accounts.</p>
      <p>Highly experienced Conveyancers with the security of full Solicitor support.</p>
    </div>
  </section>
  <span class="page-label" style="left:770px;top:1162px;">3th Page</span>

</body>
</html>
```